Electrical Contractors Business Card Design

I need a business card design for an electrical contracting business. A theme I was thinking of is the BE of Brightway Electrical both facing each other ie the second E is back to front and maybe each horizontal part of the E's are a different colours of the internal wires of TPS cable. The top would be blue(representing the sky), the middle green(representing the grass) and the lower would be brown(representing below the earth) (neutral,earth and active). And coming out of the back of each E going to each side of the business card would be the white outer sheath of TPS cable. I would like a big part of the card to be a very bright emerald flourescent green and maybe silver for the top half. the message I would like to send is that of an environmentally friendly, ethical business that delivers quality sevice on time.

Target Market(s)

40 to 80 year old home owners

Industry/Entity Type

Electrical

Contact Information for Business Card

Tom Keller
Brightway Electrical
EC 274381
Mob: 0417 592 064

```html
<!DOCTYPE html>
<html lang="en">
<head>
<meta charset="utf-8">
<title>Brightway Electrical – Business Card</title>
<link rel="stylesheet" href="https://fonts.googleapis.com/css2?family=Montserrat:wght@300;600;700&display=swap">
<style>
  :root {
    --page-bg: #e9e7e3;
    --green-bright: #3fbf4f;
    --green-deep: #1fae48;
    --grey-dark: #55575a;
    --grey-mid: #8f8d8b;
    --grey-light: #a9a6a3;
    --divider-dark: #1d1f1e;
    --silver: #e8ecea;
    --mark-dark: #2a2b2d;
    --text-light: #ffffff;
  }
  * { margin: 0; padding: 0; box-sizing: border-box; }
  html, body {
    width: 1200px;
    height: 1000px;
    overflow: hidden;
    background: var(--page-bg);
  }
  .card {
    position: absolute;
    left: 150px;
    top: 240px;
    width: 900px;
    height: 520px;
    border-radius: 44px;
    overflow: hidden;
    box-shadow: 0 14px 36px rgba(0, 0, 0, 0.22);
    font-family: "Montserrat", sans-serif;
    color: var(--text-light);
  }
  .card-art {
    position: absolute;
    inset: 0;
    width: 100%;
    height: 100%;
  }
  .brand {
    position: absolute;
    left: 150px;
    top: 60px;
    display: flex;
    align-items: center;
    gap: 26px;
  }
  .brand-dot {
    width: 150px;
    height: 150px;
    border-radius: 50%;
    background: var(--mark-dark);
  }
  .brand-name {
    font-weight: 600;
    font-size: 48px;
    letter-spacing: 0.5px;
    color: var(--text-light);
  }
  .contact {
    position: absolute;
    left: 0;
    right: 0;
    top: 340px;
    text-align: center;
    line-height: 1.25;
  }
  .contact-line {
    font-weight: 300;
    font-size: 34px;
  }
  .contact-name {
    font-weight: 700;
  }
  .phone-icon {
    width: 18px;
    height: 28px;
    vertical-align: -3px;
    margin-right: 4px;
  }
</style>
</head>
<body>
  <div class="card">
    <svg class="card-art" viewBox="0 0 900 520" preserveAspectRatio="none" aria-hidden="true">
      <defs>
        <linearGradient id="greenFill" x1="0" y1="0" x2="0" y2="1">
          <stop offset="0" stop-color="#3fbf4f"/>
          <stop offset="1" stop-color="#1fae48"/>
        </linearGradient>
        <linearGradient id="greyFill" x1="0" y1="0" x2="1" y2="0">
          <stop offset="0" stop-color="#55575a"/>
          <stop offset="0.45" stop-color="#a9a6a3"/>
          <stop offset="1" stop-color="#55575a"/>
        </linearGradient>
        <linearGradient id="silverLine" x1="0" y1="0" x2="1" y2="0">
          <stop offset="0" stop-color="#8a8f8c" stop-opacity="0"/>
          <stop offset="0.5" stop-color="#e8ecea"/>
          <stop offset="1" stop-color="#8a8f8c" stop-opacity="0"/>
        </linearGradient>
      </defs>
      <rect width="900" height="520" fill="url(#greenFill)"/>
      <g fill="#ffffff" opacity="0.06">
        <polygon points="0,40 900,110 900,140 0,70"/>
        <polygon points="0,120 900,190 900,215 0,145"/>
        <polygon points="0,200 900,270 900,290 0,220"/>
      </g>
      <polygon points="0,262 900,318 900,520 0,520" fill="url(#greyFill)"/>
      <polygon points="0,256 900,312 900,320 0,264" fill="#1d1f1e"/>
      <polygon points="80,266 820,313 820,316 80,269" fill="url(#silverLine)"/>
    </svg>

    <div class="brand">
      <div class="brand-dot"></div>
      <div class="brand-name">Brightway Electrical</div>
    </div>

    <div class="contact">
      <p class="contact-line"><span class="contact-name">Tom Keller</span> Brightway Electrical</p>
      <p class="contact-line">EC 274381</p>
      <p class="contact-line">
        <svg class="phone-icon" viewBox="0 0 18 28" aria-hidden="true">
          <rect x="1.5" y="1.5" width="15" height="25" rx="3" fill="none" stroke="#ffffff" stroke-width="2.5"/>
          <circle cx="9" cy="22" r="1.6" fill="#ffffff"/>
        </svg>0417 592 064
      </p>
    </div>
  </div>
</body>
</html>
```